Commercial Waterproofing Modern Business Cards

We are a Commercial Waterproofing company. We do a variety of jobs on the exterior of buildings. We repel from the top or scaffold to reach the areas. Cut out and recaulk expansion joints and apply sealants, brick/concrete repairs, seal window frame perimeters, and much more. Our website is www.ledgecrestfix.com.
We are looking for a new business card design that would look more modern and cutting edge. We like the transparent paper and had thought about using our logo, but maybe pulling it apart to where the building part is kind of in the background. I have attached 2 different logos that we use regularly. We want the design to be a little funky, but professional at the same time. We really don't want the logo to be incorporated by itself, but you can use the logo and take out the buildings and just use the name or vice versa. Please don't just put the logo on the card and the words around that.

Target Market(s)

Property Managers/Building Maintenance

Industry/Entity Type

Business

Contact Information for Business Card

Daniel Trovato President
Office (919)555-4827
Mobile (919)555-9306

Font styles to use
Serif

Requirements
Must have
• Nice overall design, somehow pulling from the logo for the design
Nice to have
• Look artsy and modern with a nice quality paper
Should not have
• Too many words or distracting designs. The logo 'as is'

```html
<!DOCTYPE html>
<html lang="en">
<head>
<meta charset="utf-8">
<title>LedgeCrest Fix – Business Card</title>
<link rel="stylesheet" href="https://fonts.googleapis.com/css2?family=Arvo:wght@400;700&family=Courier+Prime&display=swap">
<style>
  :root {
    --backdrop: #2b2c2e;
    --paper-light: #f1f2f2;
    --paper-mid: #e4e6e7;
    --paper-dark: #d6d9db;
    --ink-blue: #2f63b0;
    --ink-navy: #23519a;
    --ink-grey: #8a8c8e;
    --ink-phone: #6f7173;
    --wash-deep: rgba(42, 90, 158, 0.85);
    --wash-teal: rgba(111, 167, 169, 0.7);
    --wash-pale: rgba(169, 207, 208, 0);
  }
  * { box-sizing: border-box; margin: 0; padding: 0; }
  html, body { width: 1200px; height: 835px; overflow: hidden; }
  body {
    background: var(--backdrop);
    display: flex;
    align-items: center;
    justify-content: center;
  }
  .business-card {
    position: relative;
    width: 900px;
    height: 514px;
    background: linear-gradient(160deg, var(--paper-light) 0%, var(--paper-mid) 55%, var(--paper-dark) 100%);
    box-shadow: 0 14px 40px rgba(0, 0, 0, 0.45);
    overflow: hidden;
  }
  .pattern-wash {
    position: absolute;
  }
  .pattern-wash--left {
    left: -60px;
    top: 30px;
    width: 420px;
    height: 560px;
    background: radial-gradient(ellipse at 20% 65%, var(--wash-deep) 0%, var(--wash-teal) 40%, var(--wash-pale) 72%);
  }
  .pattern-wash--bottom {
    left: 200px;
    bottom: -70px;
    width: 720px;
    height: 230px;
    background: radial-gradient(ellipse at 50% 70%, var(--wash-deep) 0%, var(--wash-teal) 40%, var(--wash-pale) 72%);
  }
  .brand {
    position: absolute;
    top: 74px;
    right: 62px;
    display: flex;
    align-items: center;
    gap: 12px;
  }
  .brand-square {
    width: 22px;
    height: 22px;
    background: var(--ink-blue);
  }
  .brand-name {
    font-family: "Arvo", serif;
    font-weight: 700;
    font-size: 26px;
    color: var(--ink-blue);
  }
  .contact {
    position: absolute;
    left: 395px;
    top: 238px;
    width: 400px;
    text-align: center;
  }
  .person-name {
    font-family: "Arvo", serif;
    font-weight: 400;
    font-size: 34px;
    color: var(--ink-blue);
    line-height: 1.1;
  }
  .person-name .surname {
    font-weight: 700;
    color: var(--ink-navy);
    text-transform: uppercase;
  }
  .person-title {
    font-family: "Arvo", serif;
    font-weight: 700;
    font-size: 24px;
    color: var(--ink-grey);
    margin-top: 4px;
  }
  .phone-list {
    list-style: none;
    margin-top: 30px;
    font-family: "Courier Prime", monospace;
    font-size: 27px;
    line-height: 1.2;
    color: var(--ink-phone);
  }
  .website {
    margin-top: 8px;
    font-family: "Courier Prime", monospace;
    font-size: 20px;
    color: var(--ink-blue);
  }
</style>
</head>
<body>
  <article class="business-card">
    <div class="pattern-wash pattern-wash--left" role="img" aria-label="Flowing blue and teal water-drop pattern along the left edge"></div>
    <div class="pattern-wash pattern-wash--bottom" role="img" aria-label="Flowing blue and teal water-drop pattern along the bottom edge"></div>

    <div class="brand">
      <span class="brand-square"></span>
      <span class="brand-name">LedgeCrest Fix</span>
    </div>

    <section class="contact">
      <h1 class="person-name">Daniel <span class="surname">Trovato</span></h1>
      <p class="person-title">President Office</p>
      <ul class="phone-list">
        <li>(919)555-4827</li>
        <li>(919)555-9306</li>
      </ul>
      <p class="website">www.ledgecrestfix.com</p>
    </section>
  </article>
</body>
</html>
```